Need brochure for Verena & Company, teen theatre camp/trip to NYC

Need a really attractive, professional looking brochure to promote and describe a summer acting camp which will take teens from SF to NYC (Broadway) for workshops, shows and sightseeing.

Brochure should appeal to teens but also look polished and professional for parents. I want the cover to look like a Broadway stagefold, (with traditional yellow box, black text "stagefold")

See my website: www.verenaandcompany.example, > camps > Coast to Curtain
for content and sample look

Tri-fold brochure:
- Cover: stagefold and title of camp
- Inside left: dates, description, bullet list of what campers get to do/benefits
- Inside middle: camp itinerary
- Inside right: staff or about Verena & Company
- Outside, left (folded in): photos, testimonials
- Back center (back): direct people to website and sign-up info

Target Market(s)

Needs to appeal to teens, but also their parents

Industry/Entity Type

Performing Art

Font styles to use
Serif

Requirements
Must have
• "Stagefold" like Broadway program
• Please see my website: www.verenaandcompany.example for reference, "Coast to Curtain" page under "camps"
Nice to have
• Broadway, acting, teens, NYC skyline, etc.
• Footlight Fever jpg. gives inspiration for inside - please don't use the text content in that though
Should not have
• anything too immature or cartoony

```html
<!DOCTYPE html>
<html lang="en">
<head>
<meta charset="utf-8">
<title>Verena &amp; Company – Camp Brochure Inside</title>
<link rel="stylesheet" href="https://fonts.googleapis.com/css2?family=Abril+Fatface&family=Source+Sans+3:wght@400;600;700&family=Courier+Prime:wght@700&display=swap">
<style>
  :root{
    --yellow:#f7ea1c;
    --black:#0d0d0d;
    --ink:#1a1a1a;
    --white:#ffffff;
  }
  html,body{margin:0;padding:0;width:1200px;height:850px;overflow:hidden;background:var(--white);}
  .canvas{position:relative;width:1200px;height:850px;overflow:hidden;}
  .sheet{position:absolute;left:0;top:0;width:843px;height:596px;transform:scale(1.4235,1.4262);transform-origin:0 0;
    font-family:"Source Sans 3",Arial,sans-serif;color:var(--ink);}
  .shapes{position:absolute;left:0;top:0;width:843px;height:596px;}
  .abs{position:absolute;}

  .photo{position:absolute;border-radius:12px;overflow:hidden;}
  .photo-room{left:0;top:35px;width:210px;height:112px;background:linear-gradient(160deg,#f2ece2 0%,#d9cbb3 55%,#6b4b32 100%);}
  .photo-street{left:130px;top:135px;width:138px;height:130px;background:linear-gradient(200deg,#cfcfcf 0%,#7d7d7d 55%,#3b3b3b 100%);}

  .brand{font-family:"Source Sans 3",Arial,sans-serif;font-weight:700;color:var(--black);display:flex;align-items:center;gap:4px;white-space:nowrap;}
  .brand-dot{width:7px;height:7px;border-radius:50%;background:var(--black);}
  .brand-left{left:16px;top:202px;font-size:10.5px;}
  .brand-right{left:704px;top:44px;font-size:13px;}

  .benefits-title{left:697px;top:92px;font-size:15px;font-weight:700;letter-spacing:.3px;color:var(--black);}

  .includes-bar{left:0;top:283px;width:170px;height:24px;background:var(--yellow);border:1px dashed var(--black);border-left:none;box-sizing:border-box;
    font-size:13px;font-weight:700;line-height:22px;padding-left:18px;letter-spacing:.3px;}
  .includes-list{left:14px;top:318px;width:255px;margin:0;padding:0;list-style:none;font-size:11px;line-height:19.5px;}
  .includes-list li{position:relative;padding-left:16px;}
  .includes-list li::before{content:"";position:absolute;left:0;top:7px;width:5px;height:5px;background:var(--ink);}
  .includes-list li.plain::before{display:none;}
  .site{left:20px;top:574px;font-size:8px;letter-spacing:2px;font-weight:600;}

  .things-bar{left:283px;top:9px;width:190px;height:22px;background:var(--black);}
  .things-title{left:292px;top:9px;font-family:"Abril Fatface",Georgia,serif;font-size:15px;color:var(--white);letter-spacing:.6px;line-height:22px;}

  .itinerary{left:292px;top:40px;width:345px;font-size:7.4px;line-height:9.4px;}
  .itinerary p{margin:0 0 9px;}
  .itinerary b{font-weight:700;}

  .class-note{left:375px;top:340px;width:196px;font-size:9.2px;line-height:11.5px;}
  .show-time{left:432px;top:412px;font-size:10px;}
  .show-title{left:432px;top:424px;font-family:"Courier Prime","Courier New",monospace;font-weight:700;font-size:10.5px;line-height:12px;letter-spacing:.4px;}

  .days{left:287px;top:330px;width:180px;font-size:6.8px;line-height:8.4px;}
  .days p{margin:0 0 8px;}
</style>
</head>
<body>
<div class="canvas">
  <div class="sheet">
    <svg class="shapes" viewBox="0 0 843 596">
      <defs>
        <linearGradient id="skyline" x1="0" y1="0" x2="0" y2="1">
          <stop offset="0" stop-color="#f4f4f4"/>
          <stop offset="0.45" stop-color="#d6d6d6"/>
          <stop offset="1" stop-color="#a9a9a9"/>
        </linearGradient>
        <radialGradient id="stage" cx="0.5" cy="0.55" r="0.6">
          <stop offset="0" stop-color="#8a6b4a"/>
          <stop offset="0.6" stop-color="#3a2c22"/>
          <stop offset="1" stop-color="#111"/>
        </radialGradient>
      </defs>
      <rect width="843" height="596" fill="url(#skyline)" role="img" aria-label="Black and white photograph of the New York City skyline"/>
      <polygon points="283,0 660,0 660,596 560,596 283,300" fill="var(--yellow)" opacity="0.93"/>
      <circle cx="690" cy="55" r="105" fill="var(--black)"/>
      <circle cx="805" cy="120" r="145" fill="var(--yellow)"/>
      <circle cx="822" cy="470" r="240" fill="var(--black)"/>
      <circle cx="835" cy="478" r="220" fill="url(#stage)" role="img" aria-label="Photograph of a young actor balancing on one leg on stage while seated campers watch"/>
    </svg>

    <div class="photo photo-room" role="img" aria-label="Photograph of a bright hotel living room with a passenger jet flying past"></div>
    <div class="photo photo-street" role="img" aria-label="Photograph of Broadway street signs against city buildings"></div>

    <div class="abs brand brand-left"><span class="brand-dot"></span>Verena &amp; Company</div>
    <div class="abs brand brand-right"><span class="brand-dot"></span>Verena &amp; Company</div>
    <div class="abs benefits-title">CAMP BENEFITS</div>

    <div class="abs includes-bar">WORKSHOP INCLUDES:</div>
    <ul class="abs includes-list">
      <li>Round trip ticket from SFO to NYC (non transfer-<br>rable or changeable)</li>
      <li>Hotel accommodations for the duration of the trip</li>
      <li>Participation in 3 days of Broadway workshops</li>
      <li>A one-on-one audition feedback session with a</li>
      <li>Broadway casting Director</li>
      <li>Admission to shows on Broadway and NYC theater venues</li>
      <li>Group sightseeing excursions</li>
      <li class="plain">3 meals each day</li>
      <li>Travel to and from workshop, JFK and within NYC</li>
      <li>Fully chaperoned 24-hrs-a day</li>
    </ul>
    <div class="abs site">www.verenaandcompany.example</div>

    <div class="abs things-bar"></div>
    <div class="abs things-title">EXCITING THINGS</div>

    <div class="abs itinerary">
      <p>Sunday - Fly to NYC, check in to hotel</p>
      <p><b>Monday</b><br>10-12 - Workshop 1: Musical theatre audition prep<br>A team of Broadway professionals will break down the audition process.<br>Students will have a one-on-one session with a casting director.</p>
      <p>1:30-3 - Workshop 2: Stage Combat<br>Explore the building blocks for creating safe and believable fights on stage<br>with certified members of the Guild of Stage Combat Directors</p>
      <p><b>Tuesday</b><br>10:00am - 11:15am: Workshop #3: Voice Interpretation<br>A Broadway music director will guide students through warm-up, vocal<br>collaboration and acting through song</p>
      <p>11:30am- 12:45pm: Workshop #4: Road to Broadway<br>An intimate session with current Broadway actors about their journey from<br>High School to stage. They will even perform their audition pieces!</p>
      <p>12:45pm - 2:00pm: LUNCH</p>
      <p>2:00pm - 3:15pm: Workshop #5: Comedy Sports<br>Taught by Broadway's best writer/performers, this class helps actors cultivate<br>their creative side through improvisation, invention and story development.</p>
      <p>3:30pm - 4:45pm: Workshop #6: Acting Technique</p>
    </div>

    <div class="abs class-note">Learn to prepare scens and monologues, text analysis and collaboration. This class will give you the tools to feel confident and prepared on stage.</div>
    <div class="abs show-time">7:00pm - 9:30pm</div>
    <div class="abs show-title">BROADWAY<br>SHOW Performance</div>

    <div class="abs days">
      <p><b>Wednesday<br>July 13</b></p>
      <p>10:00am - 11:15am<br>Workshop #7<br>11:30am - 12:45pm<br>Workshop #8</p>
      <p>1-4pm - Tour Central<br>Park &amp; Times Square</p>
      <p>7pm - Shakespeare in the Park</p>
      <p><b>Thursday</b><br>9-11am - Tour of Hudson Arts University<br>2pm - Visit Statue of Liberty, Empire State Building<br>8pm - See Off-Broadway Comedy Show</p>
      <p><b>Friday</b><br>9-12 - Tour the Midtown Museum of Art<br>1-3 - Shopping<br>4pm - Leave for airport, return to SFO</p>
    </div>
  </div>
</div>
</body>
</html>
```